Leaf Haven Business Card Design

My E-Commerce store is called Leaf Haven

Website address is - http://www.leafhaven-demo.com.au

I would like a colourful, friendly business with the description in the 'must haves' box incorporated into it
Updates

Please add the following to the business cards; Natural & Organic Products Online Organic Pantry Items Superfoods & Supplements Natural Skincare Eco Friendly Household Products

Industry/Entity Type

Business

Contact Information for Business Card

www.leafhaven-demo.com.au
mira@leafhaven-demo.com.au

Colors
acd037
9bcb3c
cadf82
eaf2ce

Requirements
Must have
• Natural & Organic Eco Products Online.
• Leaf Haven specialises in organic pantry items, superfoods and supplements, organic skincare for you and your family & eco friendly household products.

```html
<!DOCTYPE html>
<html lang="en">
<head>
<meta charset="utf-8">
<title>Leaf Haven Business Card</title>
<link rel="stylesheet" href="https://fonts.googleapis.com/css2?family=Lato:wght@400;700&display=swap">
<style>
  :root {
    --page-bg: #e9e7e3;
    --card-light: #ffffff;
    --card-dark: #262626;
    --brand-green: #1fa04a;
    --name-green: #3aaa4a;
    --text-grey: #7a7a7a;
    --text-light: #cfcfcf;
    --accent-soft: #9bcb3c;
    --accent-pale: #cadf82;
  }
  * { margin: 0; padding: 0; box-sizing: border-box; }
  html, body {
    width: 1200px;
    height: 1000px;
    overflow: hidden;
    background: var(--page-bg);
    font-family: "Lato", Arial, sans-serif;
  }
  .card {
    position: absolute;
    left: 276px;
    width: 648px;
    height: 371px;
    border-radius: 22px;
    overflow: hidden;
  }
  .card--front { top: 113px; background: var(--card-light); box-shadow: 0 4px 14px rgba(0,0,0,.12); }
  .card--back { top: 517px; background: var(--card-dark); box-shadow: 0 4px 14px rgba(0,0,0,.2); }

  .holder { position: absolute; left: 40px; top: 42px; }
  .holder__name { font-size: 19px; font-weight: 700; color: var(--name-green); line-height: 1.2; }
  .holder__role { font-size: 14px; color: var(--text-grey); margin-top: 1px; }

  .contact { position: absolute; left: 40px; top: 111px; list-style: none; }
  .contact__item {
    display: flex; align-items: center; gap: 6px;
    font-size: 15px; color: var(--text-grey);
    height: 25px;
  }
  .contact__icon { width: 12px; height: 12px; flex: none; }

  .range { position: absolute; left: 40px; top: 214px; width: 280px; }
  .range__title { font-size: 13px; font-weight: 700; color: var(--name-green); margin-bottom: 5px; }
  .range__list { list-style: none; }
  .range__item {
    display: flex; align-items: center; gap: 7px;
    font-size: 12.5px; color: var(--text-grey);
    height: 19px;
  }
  .range__item::before {
    content: ""; width: 6px; height: 6px; border-radius: 50%;
    background: var(--accent-soft); flex: none;
  }

  .brand {
    display: flex; align-items: center; gap: 12px;
    color: var(--brand-green);
    font-weight: 400;
    white-space: nowrap;
  }
  .brand__dot { border-radius: 50%; background: var(--accent-soft); flex: none; }
  .card--front .brand { position: absolute; right: 26px; bottom: 34px; font-size: 46px; }
  .card--front .brand__dot { width: 22px; height: 22px; }

  .back-content {
    position: absolute; inset: 0;
    display: flex; flex-direction: column; align-items: center; justify-content: center;
    text-align: center; padding: 0 70px;
  }
  .card--back .brand { font-size: 54px; }
  .card--back .brand__dot { width: 26px; height: 26px; }
  .tagline {
    margin-top: 14px;
    font-size: 16px; font-weight: 700; color: var(--accent-pale);
  }
  .about {
    margin-top: 10px;
    font-size: 13px; line-height: 1.5; color: var(--text-light);
    max-width: 470px;
  }
</style>
</head>
<body>

<section class="card card--front">
  <div class="holder">
    <p class="holder__name">Daniel Reed</p>
    <p class="holder__role">Founder &amp; CEO</p>
  </div>
  <ul class="contact">
    <li class="contact__item">
      <svg class="contact__icon" viewBox="0 0 24 24"><path fill="#1fa04a" d="M6.6 10.8a15.1 15.1 0 0 0 6.6 6.6l2.2-2.2c.3-.3.7-.4 1-.2 1.1.4 2.3.6 3.6.6.6 0 1 .4 1 1V20c0 .6-.4 1-1 1A17 17 0 0 1 3 4c0-.6.4-1 1-1h3.5c.6 0 1 .4 1 1 0 1.3.2 2.5.6 3.6.1.3 0 .7-.2 1z"/></svg>
      013 246 8579
    </li>
    <li class="contact__item">
      <svg class="contact__icon" viewBox="0 0 24 24"><rect x="2" y="5" width="20" height="14" fill="#1fa04a"/><path d="M2 5l10 8 10-8" fill="none" stroke="#fff" stroke-width="2"/></svg>
      mira@leafhaven-demo.com.au
    </li>
    <li class="contact__item">
      <svg class="contact__icon" viewBox="0 0 24 24" fill="none" stroke="#1fa04a" stroke-width="2"><circle cx="12" cy="12" r="10"/><ellipse cx="12" cy="12" rx="4" ry="10"/><path d="M2 12h20"/></svg>
      www.leafhaven-demo.com.au
    </li>
  </ul>
  <div class="range">
    <p class="range__title">Natural &amp; Organic Products Online</p>
    <ul class="range__list">
      <li class="range__item">Organic Pantry Items</li>
      <li class="range__item">Superfoods &amp; Supplements</li>
      <li class="range__item">Natural Skincare</li>
      <li class="range__item">Eco Friendly Household Products</li>
    </ul>
  </div>
  <div class="brand">
    <span class="brand__dot"></span>
    <span class="brand__name">Leaf Haven</span>
  </div>
</section>

<section class="card card--back">
  <div class="back-content">
    <div class="brand">
      <span class="brand__dot"></span>
      <span class="brand__name">Leaf Haven</span>
    </div>
    <p class="tagline">Natural &amp; Organic Eco Products Online.</p>
    <p class="about">Leaf Haven specialises in organic pantry items, superfoods and supplements, organic skincare for you and your family &amp; eco friendly household products.</p>
  </div>
</section>

</body>
</html>
```